Shiatsu in der Kindlichen Entwicklung
Zielgruppe
Frauen, Familien
Aufgabenstellung
Es sollte ein buntes, gemaltes (Buntstift) aber trotzedem elegantes und ansprechendes Desigen haben.
Ich stelle mir einen Flyer vor, der ein Cover hat und kombinierbare einzelnen Seiten, die man dazu stecken kann. Je nach Interesse meiner Kunden.
Jedes Thema hat eine eigene Seite: Shiatsu in der Schwangerschaft, Baby Shiatsu und Kinder Shiatsu, Shiatsu in der Schule, Shiatsu Kurse usw. die dem Flyer beigefügt werden können.
Ich begleite Famielien und Kinder von klein bis gross.
Es sollten drei Abschnitte sein:
1. Shiatsu in der Schwangerschaft
2. Baby Shiatsu
3. Shiatsu mit Kindern

```html
<!DOCTYPE html>
<html lang="de">
<head>
<meta charset="utf-8">
<title>Shiatsu Flyer – Cover und Zusatzblätter</title>
<link rel="stylesheet" href="https://fonts.googleapis.com/css2?family=Amatic+SC:wght@700&family=Ubuntu:wght@400;500;700&display=swap">
<style>
  :root{
    --bg:#ffffff;
    --yellow:#f8f3a4;
    --red:#ef3a5d;
    --green:#84c274;
    --green-text:#6cbf5a;
    --pink:#d497c6;
    --pink-text:#c98bbd;
    --orange:#ef7b55;
    --orange-text:#ec6d49;
    --text:#3b3b3b;
    --label:#111111;
  }
  *{box-sizing:border-box;margin:0;padding:0}
  html,body{width:1059px;height:1200px;overflow:hidden;background:var(--bg)}
  body{position:relative;font-family:"Ubuntu",sans-serif;color:var(--text)}

  .sheet{position:absolute;width:249px;height:497px;background:#fff;box-shadow:0 1px 4px rgba(0,0,0,.28);overflow:hidden}
  .hand{font-family:"Amatic SC",cursive;font-weight:700;text-transform:uppercase;letter-spacing:.3px;line-height:1}

  /* Cover */
  .cover{left:396px;top:26px}
  .cover__head{position:absolute;left:0;top:0;width:100%;height:178px;background:var(--yellow);border-bottom:4px solid var(--red);text-align:center;color:var(--red)}
  .cover__line{position:absolute;left:0;width:100%;font-size:29px}
  .cover__line--1{top:12px;padding-left:16px}
  .cover__line--2{top:44px;padding-left:4px}
  .cover__rule{position:absolute;top:80px;left:30px;width:188px;height:2px;background:var(--red)}
  .cover__line--3{top:91px;padding-left:4px}
  .cover__photo{position:absolute;left:0;top:181px;width:100%;height:276px;background:linear-gradient(160deg,#f3c9a8 0%,#f6e6da 40%,#ffffff 55%,#5fc4d8 75%,#9cc850 100%)}
  .cover__band{position:absolute;left:0;top:457px;width:100%;height:3px;background:var(--red)}

  .butterfly{position:absolute;border-radius:50%;opacity:.5}

  .caption{position:absolute;font-family:"Ubuntu",sans-serif;font-weight:700;font-size:13px;color:var(--label)}

  /* Topic sheets */
  .topic__head{position:absolute;left:0;top:0;width:100%;color:#fff;text-align:center;display:flex;align-items:center;justify-content:center;font-size:27px;line-height:1.12}
  .topic__photo{position:absolute;left:0;width:100%}
  .topic__intro{position:absolute;left:30px;width:184px;font-size:7.9px;line-height:10.1px}
  .topic__title{position:absolute;left:30px;font-size:27px}
  .topic__list{position:absolute;left:28px;list-style:none;font-size:7.9px;line-height:12.5px}
  .topic__list li::before{content:"• "}
  .topic__list .cont{padding-left:5px}
  .topic__list .cont::before{content:""}

  .pregnancy{left:86px;top:630px}
  .pregnancy .topic__head{height:80px;background:var(--green)}
  .pregnancy .topic__photo{top:80px;height:130px;border-bottom:3px solid var(--green);background:linear-gradient(110deg,#ffffff 0%,#f1d2bd 35%,#e8b999 60%,#f7ece4 100%)}
  .pregnancy .topic__title{color:var(--green-text);top:338px}

  .baby{left:391px;top:630px}
  .baby .topic__head{height:56px;background:var(--pink)}
  .baby .topic__photo{top:56px;height:152px;border-bottom:3px solid var(--pink);background:linear-gradient(100deg,#f7f2ee 0%,#f4d7c6 45%,#eec5ac 70%,#f6e2d4 100%)}
  .baby .topic__title{color:var(--pink-text);top:311px}

  .kids{left:707px;top:630px}
  .kids .topic__head{height:56px;background:var(--orange)}
  .kids .topic__photo{top:56px;height:152px;border-bottom:3px solid var(--orange);background:linear-gradient(120deg,#eeeeee 0%,#f5f5f5 35%,#e9d2c3 60%,#e6d8dc 100%)}
  .kids .topic__title{color:var(--orange-text);top:290px}
</style>
</head>
<body>

<section class="sheet cover">
  <header class="cover__head">
    <div class="cover__line cover__line--1 hand">Praxis für</div>
    <div class="cover__line cover__line--2 hand">Vernöstliche Medizin</div>
    <div class="cover__rule"></div>
    <div class="cover__line cover__line--3 hand">TCM &amp; Shiatsu</div>
    <div class="butterfly" role="img" aria-label="Gemalter Schmetterling" style="left:9px;top:9px;width:32px;height:22px;background:#f28aa0"></div>
  </header>
  <div class="cover__photo" role="img" aria-label="Foto: vier lachende Kinder schauen von oben in die Kamera"></div>
  <div class="cover__band"></div>
</section>
<div class="caption" style="left:706px;top:245px">Cover Flyer</div>

<section class="sheet pregnancy">
  <h2 class="topic__head hand">Shiatsu in der<br>Schwangerschaft</h2>
  <div class="topic__photo" role="img" aria-label="Foto: Hände auf dem Bauch einer Schwangeren"></div>
  <p class="topic__intro" style="top:227px">Wussten Sie, dass Shiatsu eine wunderbare Methode ist während der Schwangerschaft? Es wirkt unterstützend, begleitend, geburts­vorbereitend und sehr entspannend. Diese Ruhe gibt den nötigen Raum, den oftmals kräfteraubenden Alltag auszublenden und wieder in den eigenen Körper zu lauschen. Dabei findet eine natürliche und innige Verbindung mit dem Baby statt. Das ist kraftspendend und harmonisierend.</p>
  <h3 class="topic__title hand">Anwendung</h3>
  <ul class="topic__list" style="top:375px">
    <li>Morgendlicher Übelkeit</li>
    <li>Rückenschmerzen</li>
    <li>Wassereinlagerungen</li>
    <li>Schlafprobleme</li>
    <li>Freude</li>
    <li>Sorge</li>
    <li>Ängste</li>
    <li>Erfahrungen vorangegangener Geburten</li>
    <li>Partnerübungen für alle Phasen der Geburt</li>
  </ul>
  <div class="butterfly" role="img" aria-label="Gemalter Schmetterling in Orange und Grün" style="left:165px;top:380px;width:62px;height:42px;background:linear-gradient(90deg,#f39a7a,#9fd48e)"></div>
</section>

<section class="sheet baby">
  <h2 class="topic__head hand">Baby Shiatsu</h2>
  <div class="topic__photo" role="img" aria-label="Foto: Hände massieren sanft ein liegendes Baby"></div>
  <div class="butterfly" role="img" aria-label="Gemalter Schmetterling in Türkis" style="left:22px;top:62px;width:70px;height:44px;background:#8fdcec"></div>
  <p class="topic__intro" style="top:227px">Auf diese angenehme und sanfte Behandlung sprechen gerade Babys mit ihren feinsinnigen Empfindungen besonders gut an. Speziell für sie wurde velani•Baby Shiatsu® entwickelt, dass ausdrücklich auf die Bedürfnisse und Wünsche der Kleinsten eingeht und sie in der Entwicklung fördert.</p>
  <h3 class="topic__title hand">Vorteile</h3>
  <ul class="topic__list" style="top:345px">
    <li>unterstützt die Entwicklung des Kindes</li>
    <li>vertieft den Kontakt und stärkt die Bindung von</li>
    <li class="cont">Mutter und Baby</li>
    <li>hilfreich bei Schlafstörungen, Blähungen, etc.</li>
    <li>kann selbst erlernt &amp; zuhause umgesetzt werden</li>
    <li>richtet das Baby durch Streicheleinheiten auf</li>
    <li>ist gut für die Haltung, Gesundheit</li>
    <li class="cont">und emotionale Stabilität</li>
    <li>optimiert die Wahrnehmung</li>
  </ul>
</section>

<section class="sheet kids">
  <h2 class="topic__head hand">Shiatsu mit Kindern</h2>
  <div class="topic__photo" role="img" aria-label="Foto: Mädchen mit Blume auf einem weißen Korbstuhl"></div>
  <p class="topic__intro" style="top:228px;line-height:12.4px;width:186px">Kaminari Programm ist ein Schulprogramm für Primarschüler und Kinder bis zum Alter von etwa zwölf Jahren. Es setzt sich zusammen aus der Behandlungssequenz Kaminari-Shiatsu.</p>
  <h3 class="topic__title hand">Ziele</h3>
  <ul class="topic__list" style="top:324px">
    <li>die Gesundheit zu fördern</li>
    <li>die Konzentrationsfähigkeit zu verbessern</li>
    <li>eine gesunde Haltung zu unterstützen</li>
    <li>das Klassenklima zu verbessern</li>
    <li>die Selbstwirksamkeit zu verbessern</li>
    <li>ist eine Einführung in die</li>
    <li class="cont">japanische Kultur und Sprache</li>
    <li>und macht Alt und Jung</li>
    <li class="cont">riesen grossen Spass</li>
  </ul>
  <div class="butterfly" role="img" aria-label="Gemalter Schmetterling in Grün und Orange" style="left:142px;top:412px;width:98px;height:62px;background:linear-gradient(90deg,#9fd48e,#f39a7a)"></div>
</section>

<div class="caption" style="left:457px;top:1152px">Zusatzblätter</div>

</body>
</html>
```